Harbor Wick Co Banner Ad for Upcoming holidays

We would like for you to design an ad for Memorial day and Father's Day. For Memorial Day the sale will be 25% OFF select candles and free shipping when you order $50 or more.
For father's day the deal will be get 30% off all candles and free shipping when you order $75 or more.
Please note: These banners will be on our website, they do not require our logo.Banner size: 314 height x 783 width

Industry/Entity Type

Shipping

Requirements
Must have
• Banner size: 314 height x 783 width
Nice to have
• Picture of our unforgettable candle
Should not have
• Logo

```html
<!DOCTYPE html>
<html lang="en">
<head>
<meta charset="utf-8">
<title>Harbor Wick Co – Happy Father's Day Sale Banner</title>
<link rel="stylesheet" href="https://fonts.googleapis.com/css2?family=Oswald:wght@500&family=Lobster&display=swap">
<style>
  :root {
    --teal: #3f7987;
    --teal-dark: #2f6673;
    --teal-ink: #2d7280;
    --white: #ffffff;
    --badge-line: #8fc3c6;
    --photo-warm: #d9cdbd;
    --photo-deep: #4f5e4a;
  }
  html, body {
    margin: 0;
    padding: 0;
    overflow: hidden;
  }
  body {
    width: 1200px;
    height: 2992px;
  }
  .banner {
    position: relative;
    width: 1200px;
    height: 2992px;
    background: var(--teal);
    overflow: hidden;
    font-family: "Oswald", "Arial Narrow", sans-serif;
    color: var(--white);
  }
  .badge {
    position: absolute;
    left: 0;
    top: 0;
  }
  .badge-title {
    position: absolute;
    left: 267px;
    width: 669px;
    top: 250px;
    margin: 0;
    text-align: center;
    font-family: "Lobster", cursive;
    font-weight: 400;
    font-size: 128px;
    line-height: 168px;
    color: var(--teal-ink);
  }
  .offer-heading {
    position: absolute;
    left: 0;
    width: 1200px;
    margin: 0;
    text-align: center;
    font-weight: 500;
    font-size: 108px;
    line-height: 1;
    letter-spacing: 1px;
    text-transform: uppercase;
  }
  .offer-heading.memorial { top: 1042px; }
  .offer-heading.fathers { top: 1726px; }
  .heading-rule {
    position: absolute;
    height: 5px;
    background: var(--white);
  }
  .heading-rule.memorial { left: 229px; width: 745px; top: 1194px; }
  .heading-rule.fathers { left: 268px; width: 668px; top: 1870px; }
  .discount {
    position: absolute;
    left: 76px;
    display: flex;
    align-items: center;
    font-weight: 500;
  }
  .discount.memorial { top: 1370px; }
  .discount.fathers { top: 2048px; }
  .discount .percent {
    font-size: 164px;
    line-height: 1;
  }
  .discount .off {
    font-size: 62px;
    margin-left: 34px;
    margin-top: -28px;
  }
  .divider {
    position: absolute;
    left: 609px;
    width: 4px;
    background: var(--white);
  }
  .divider.memorial { top: 1262px; height: 384px; }
  .divider.fathers { top: 1946px; height: 384px; }
  .terms {
    position: absolute;
    left: 657px;
    margin: 0;
    font-weight: 500;
    font-size: 56px;
    line-height: 76px;
    text-transform: uppercase;
  }
  .terms.memorial { top: 1262px; }
  .terms.fathers { top: 1946px; }
  .product-photo {
    position: absolute;
    background: var(--white);
    padding: 22px;
    box-sizing: border-box;
    box-shadow: 0 6px 18px rgba(0,0,0,0.25);
  }
  .product-photo .fill {
    width: 100%;
    height: 100%;
    background: linear-gradient(160deg, var(--photo-warm) 0%, #b9b3a4 40%, var(--photo-deep) 70%, var(--photo-warm) 100%);
  }
  .product-photo.first {
    left: 40px; top: 2390px; width: 530px; height: 540px;
    transform: rotate(-3deg);
  }
  .product-photo.second {
    left: 630px; top: 2400px; width: 530px; height: 540px;
    transform: rotate(4deg);
  }
</style>
</head>
<body>
<main class="banner">
  <svg class="badge" width="1200" height="960" viewBox="0 0 1200 960" aria-hidden="true">
    <path d="M420 70 H780 Q800 150 900 165 V390 Q870 470 900 550 V790 Q800 805 780 900 H420 Q400 805 300 790 V550 Q330 470 300 390 V165 Q400 150 420 70 Z"
          fill="var(--white)"/>
    <path d="M438 96 H762 Q784 172 874 186 V392 Q846 470 874 548 V772 Q784 786 762 874 H438 Q416 786 326 772 V548 Q354 470 326 392 V186 Q416 172 438 96 Z"
          fill="none" stroke="var(--badge-line)" stroke-width="5"/>
  </svg>
  <h1 class="badge-title">Happy<br>Father's<br>Day</h1>

  <h2 class="offer-heading memorial">For Memorial Day</h2>
  <div class="heading-rule memorial"></div>
  <div class="discount memorial"><span class="percent">25%</span><span class="off">OFF</span></div>
  <div class="divider memorial"></div>
  <p class="terms memorial">For selected<br>candles and<br>free shipping<br>when you order<br>$50 or more</p>

  <h2 class="offer-heading fathers">For Father's Day</h2>
  <div class="heading-rule fathers"></div>
  <div class="discount fathers"><span class="percent">30%</span><span class="off">OFF</span></div>
  <div class="divider fathers"></div>
  <p class="terms fathers">For selected<br>candles and<br>free shipping<br>when you order<br>$75 or more</p>

  <div class="product-photo first">
    <div class="fill" role="img" aria-label="Photo of a lit three-wick Harbor Wick Co candle in a glass jar with a palm tree label and silver lid"></div>
  </div>
  <div class="product-photo second">
    <div class="fill" role="img" aria-label="Photo of a Harbor Wick Co three-wick candle with its silver lid leaning beside it"></div>
  </div>
</main>
</body>
</html>
```